Flyer-Design für ein Cateringunternehmen
Zielgruppe
Wir sind ein Cateringunternehmen, welches Hochzeiten, Firmenfeiern, Events, Geburtstage, Schuleinführungsfeiern etc. beliefert.
Aufgabenstellung
Das Design sollte DIN lang sein, bitte den Flyer mit dunklem Hintergrund erstellen, er soll möglichst edel wirken, da wir viele Hochzeiten beliefern
Folgende Daten sollten auf dem Flyer sein: TAFELWERK Dresden, Lindenhofweg 14, 01239 Dresden, www.tafelwerk-beispiel.de, info@tafelwerk-beispiel.de , Telefon: 0351-5839146, Fax: 0351-5839147, Mobil: 0162-7385021

```html
<!DOCTYPE html>
<html lang="de">
<head>
<meta charset="utf-8">
<title>TAFELWERK Dresden – Flyer</title>
<link rel="stylesheet" href="https://fonts.googleapis.com/css2?family=Prata&display=swap">
<style>
  :root {
    --ink: #ffffff;
    --night: #030303;
    --night-soft: #0c0b0a;
    --skyline: #1a1c20;
    --window-glow: rgba(214, 170, 110, 0.30);
    --street-glow: rgba(190, 120, 45, 0.55);
    --cool-glow: rgba(150, 175, 190, 0.22);
    --tower-shade: rgba(40, 38, 36, 0.55);
  }
  * { margin: 0; padding: 0; box-sizing: border-box; }
  html, body {
    width: 1200px;
    height: 2400px;
    overflow: hidden;
    background: var(--night);
  }
  .flyer {
    position: relative;
    width: 1200px;
    height: 2400px;
    overflow: hidden;
    font-family: "Prata", Georgia, serif;
    color: var(--ink);
  }
  .city-backdrop {
    position: absolute;
    inset: 0;
    background:
      radial-gradient(ellipse 90px 700px at 1090px 1550px, var(--street-glow), transparent 75%),
      radial-gradient(ellipse 260px 900px at 1060px 1500px, rgba(150, 95, 35, 0.35), transparent 70%),
      radial-gradient(ellipse 160px 420px at 750px 1520px, var(--cool-glow), transparent 75%),
      radial-gradient(ellipse 150px 520px at 620px 1080px, var(--window-glow), transparent 75%),
      radial-gradient(ellipse 140px 380px at 160px 820px, rgba(200, 170, 120, 0.22), transparent 75%),
      radial-gradient(ellipse 200px 460px at 360px 900px, rgba(170, 140, 100, 0.18), transparent 75%),
      radial-gradient(ellipse 520px 420px at 300px 1650px, var(--tower-shade), transparent 75%),
      radial-gradient(ellipse 700px 600px at 560px 1250px, rgba(95, 80, 60, 0.35), transparent 72%),
      linear-gradient(180deg, var(--night) 0%, var(--night) 12%, var(--skyline) 32%, #221d17 55%, #17130f 72%, var(--night-soft) 86%, var(--night) 100%);
  }
  .text-shade {
    position: absolute;
    left: 0;
    right: 0;
    top: 1700px;
    height: 700px;
    background: radial-gradient(ellipse 520px 380px at 600px 2050px, rgba(0, 0, 0, 0.55), transparent 75%);
  }
  .brand-name {
    position: absolute;
    top: 372px;
    left: 0;
    width: 100%;
    text-align: center;
    font-family: "Prata", Georgia, serif;
    font-weight: 400;
    font-size: 132px;
    line-height: 1;
    letter-spacing: -2px;
  }
  .contact {
    position: absolute;
    top: 1784px;
    left: 0;
    width: 100%;
    text-align: center;
    font-size: 36px;
    line-height: 46px;
  }
  .contact p + p { margin-top: 40px; }
</style>
</head>
<body>
  <main class="flyer">
    <div class="city-backdrop" role="img" aria-label="Nächtliche Stadtansicht mit beleuchteten Hochhäusern und einer von Laternen erhellten Straße"></div>
    <div class="text-shade"></div>

    <h1 class="brand-name">TAFELWERK</h1>

    <section class="contact">
      <p>TAFELWERK Dresden</p>
      <p>Lindenhofweg 14<br>01239 Dresden</p>
      <p>www.tafelwerk-beispiel.de<br>info@tafelwerk-beispiel.de</p>
      <p>Telefon: 0351-5839146<br>Fax: 0351-5839147<br>Mobil: 0162-7385021</p>
    </section>
  </main>
</body>
</html>
```